Stylise 5 diagrams to feature on webpage

We need existing diagrams recreated in a stylized format to go on our web page.

We will provide all required drafts and are after a style/design set which will work with our brand identity, target market and existing website.

Company Background
- We are a provider of data, software and services which blue chip companies use to shape their customer experience. ie very high tier companies, so our audience are of a high calibre.

What we want to present is clarity of thought, expertise and authority (ie we deal in data so a certain amount of conservatism is required to inspire trust in our data). However we dont want this to appear old and 'stuffy'. We want to present as the savvy partner who know their stuff but at the same time are modern and innovative and fresh.
So I am imagining crisp, clean, slick and innovative.

Potential for ongoing work
This project will have a number of images to recreate initially. However we will need an ongoing service/provider which can duplicate the style.
Other pieces may include designing PPT templates, presentations, reports, web, brochures etc

Website that the diagrams will live within.
http://new.quillmarkdata.com.au/ this is the start of the new web page. the images will sit inside the content and will need to 'balance' the currently high text to image ratio and work with the existing logo and style.
Please don't let the existing website limit your creativity or inspiration - we are open to improving our design elements :) What I do want to retain in alignment with the website is simplicity and 'crisp', ie use of clean fonts and sharp colours.

Attached are our existing brand guides. Again, please observe these loosely but feel free to offer up any improvements. The key here is that the Aubergine key colour is respected.

NOTE: Both attached files are the same but in different formats as some were having troubles opening.

Target Market(s)

Target Market(s)
- Executives of large blue chip companies (think airlines, telcos, etc).
- Consulting firms (think Hollingford Brackett, RTVW, Garrowby)

Industry/Entity Type

Software

Requirements
Must have
• Must haves
- PSD editable format for text, graphics, all elements
- the diagrams required must look to be of the same design 'family'. Once we establish this style we can progress to develop all the required diagrams and in future create a rship where we develop additional company collateral

```html
<!DOCTYPE html>
<html lang="en">
<head>
<meta charset="utf-8">
<title>Net Advocate System diagrams</title>
<link href="https://fonts.googleapis.com/css2?family=Source+Sans+3:wght@400;600;700;800&display=swap" rel="stylesheet">
<style>
  :root {
    --aubergine: #8e3f6f;
    --aubergine-dark: #6e2d55;
    --aubergine-light: #b46a96;
    --blush: #ecdbe4;
    --brick: #8a2f2c;
    --grey-dark: #555;
    --grey-mid: #8a8a8a;
    --grey-light: #d9d9d9;
    --grey-pale: #efefef;
    --ink: #333;
    --gold: #e6c21c;
    --green: #2f8a3c;
    --white: #fff;
  }
  * { box-sizing: border-box; margin: 0; padding: 0; }
  html, body { width: 707px; height: 1200px; overflow: hidden; background: var(--white); }
  body { font-family: "Source Sans 3", Arial, sans-serif; color: var(--ink); }
  .canvas { position: relative; width: 707px; height: 1200px; overflow: hidden; }

  .cycle { position: absolute; left: 40px; top: 4px; width: 270px; height: 256px; }
  .cycle-label { font-size: 15px; font-weight: 700; fill: var(--white); }

  .model-box { position: absolute; top: 308px; height: 162px; overflow: hidden; }
  .model-box svg { position: absolute; inset: 0; }
  .model-left { left: 20px; width: 300px; }
  .model-right { left: 336px; width: 339px; }
  .model-text { position: absolute; font-size: 11.5px; line-height: 1.22; }
  .model-text strong { font-weight: 700; }
  .top-down { left: 70px; top: 16px; width: 190px; text-align: center; color: var(--white); }
  .bottom-up { left: 168px; top: 104px; width: 125px; text-align: center; }
  .bullet-list { list-style: none; position: absolute; left: 12px; width: 320px; font-size: 11px; line-height: 1.2; }
  .bullet-list li::before { content: "• "; }
  .bullet-list strong { color: var(--aubergine-dark); }
  .bullets-top { top: 6px; color: var(--white); }
  .bullets-top strong { color: var(--white); }
  .bullets-bottom { top: 92px; }

  .segments { position: absolute; left: 60px; top: 528px; width: 575px; height: 108px;
    background: linear-gradient(90deg,
      var(--brick) 0 84px, #a8a8a8 84px 96px, #c9c9c9 96px 290px, #b5b5b5 290px 302px,
      var(--gold) 302px 388px, #c9c9c9 388px 420px,
      var(--green) 420px 520px, #c9c9c9 520px 555px, transparent 555px);
    border-radius: 34px 34px 0 0; }
  .segment-label { position: absolute; top: 612px; font-size: 17px; font-weight: 600; color: var(--white); }
  .label-detractors { left: 62px; }
  .label-passives { left: 372px; }
  .label-promoters { left: 486px; }
  .score-bar { position: absolute; left: 52px; top: 636px; width: 590px; height: 44px;
    background: linear-gradient(#f4f4f4, #cfcfcf); border-radius: 6px;
    display: flex; align-items: center; font-size: 19px; font-weight: 700; }
  .score-name { margin-left: 28px; width: 230px; color: var(--grey-mid); }
  .score-op { color: var(--grey-mid); width: 40px; text-align: center; }
  .score-promoters { color: var(--green); width: 140px; text-align: center; }
  .score-detractors { color: var(--brick); margin-left: 6px; }

  .system { position: absolute; left: 53px; top: 757px; width: 592px; height: 406px;
    background: linear-gradient(#f2f2f2, #e4e4e4); border-radius: 8px; }
  .system-title { height: 48px; border-radius: 8px 8px 0 0;
    background: linear-gradient(var(--aubergine-light), var(--aubergine));
    color: var(--white); font-size: 25px; font-weight: 800; text-align: center; line-height: 48px; }
  .step-title { position: absolute; font-size: 17px; font-weight: 400; color: var(--grey-dark); }
  .step-title b { color: var(--brick); font-weight: 800; }
  .step-1 { left: 44px; top: 66px; }
  .step-2 { left: 352px; top: 66px; }
  .step-3 { left: 0; width: 100%; text-align: center; top: 222px; }

  .sentiment { position: absolute; top: 92px; width: 60px; text-align: center; }
  .sentiment-icon { width: 44px; height: 44px; margin: 0 auto 6px; border-radius: 50%; background: var(--grey-light); }
  .tag { display: inline-block; background: var(--grey-dark); color: var(--white); font-size: 11px; font-weight: 600; padding: 2px 6px; }
  .s-promoters { left: 12px; } .s-passives { left: 88px; } .s-detractors { left: 164px; }

  .customer-figure { position: absolute; left: 322px; top: 96px; width: 60px; height: 70px; background: linear-gradient(#7a7a7a, #555); border-radius: 28px 28px 6px 6px; }
  .customer-label { position: absolute; left: 318px; top: 172px; font-size: 13px; font-weight: 600; color: var(--grey-dark); }
  .dialogue { position: absolute; left: 390px; top: 132px; font-size: 12px; color: var(--grey-dark); }
  .loop-lines { position: absolute; left: 438px; top: 100px; }
  .role-box { position: absolute; left: 468px; width: 94px; height: 26px; background: var(--grey-dark); color: var(--white); font-size: 13px; font-weight: 600; text-align: center; line-height: 26px; }
  .r1 { top: 96px; } .r2 { top: 129px; } .r3 { top: 162px; }
  .learn { position: absolute; left: 570px; top: 96px; writing-mode: vertical-rl; font-size: 11px; color: var(--grey-dark); font-weight: 600; }

  .priority { position: absolute; top: 252px; text-align: center; font-size: 13px; font-weight: 600; color: var(--grey-dark); line-height: 1.2; }
  .priority svg, .priority .advocate-icon { display: block; margin: 0 auto 6px; }
  .p-sight { left: 50px; width: 130px; }
  .p-champions { left: 214px; width: 150px; }
  .p-report { left: 386px; width: 170px; }
  .advocate-icon { position: relative; width: 70px; height: 78px; }
  .advocate-head { position: absolute; left: 0; top: 24px; width: 50px; height: 50px; border-radius: 50%; background: var(--grey-light); }
  .advocate-bubble { position: absolute; right: 0; top: 0; width: 30px; height: 24px; border: 2px solid var(--grey-dark); border-radius: 50%; background: var(--white); font-size: 9px; font-weight: 700; line-height: 20px; }
</style>
</head>
<body>
<main class="canvas">

  <svg class="cycle" viewBox="0 0 270 256" aria-label="Listen, Act, Discover, Improve cycle">
    <defs>
      <linearGradient id="arrow-purple" x1="0" y1="0" x2="0" y2="1">
        <stop offset="0" stop-color="#b05d8d"/><stop offset="1" stop-color="#7a3160"/>
      </linearGradient>
      <linearGradient id="arrow-grey" x1="0" y1="0" x2="0" y2="1">
        <stop offset="0" stop-color="#e2e2e2"/><stop offset="1" stop-color="#8f8f8f"/>
      </linearGradient>
      <path id="cycle-arrow" d="M-78 -19 H52 V-32 L86 0 L52 32 V19 H-78 Z"/>
    </defs>
    <g transform="translate(192 70) rotate(45)">
      <use href="#cycle-arrow" fill="url(#arrow-purple)"/>
      <text class="cycle-label" x="-12" y="5" text-anchor="middle">Listen</text>
    </g>
    <g transform="translate(192 184) rotate(135)">
      <use href="#cycle-arrow" fill="url(#arrow-grey)"/>
      <text class="cycle-label" x="-12" y="-5" text-anchor="middle" transform="rotate(180)" style="fill:#333">Act</text>
    </g>
    <g transform="translate(78 184) rotate(225)">
      <use href="#cycle-arrow" fill="url(#arrow-purple)"/>
      <text class="cycle-label" x="12" y="5" text-anchor="middle" transform="rotate(180)">Discover</text>
    </g>
    <g transform="translate(78 70) rotate(-45)">
      <use href="#cycle-arrow" fill="url(#arrow-grey)"/>
      <text class="cycle-label" x="-12" y="5" text-anchor="middle" style="fill:#333">Improve</text>
    </g>
  </svg>

  <section class="model-box model-left">
    <svg width="300" height="162" aria-hidden="true">
      <defs>
        <linearGradient id="grey-fade" x1="0" y1="0" x2="0" y2="1">
          <stop offset="0" stop-color="#cfcfcf"/><stop offset="1" stop-color="#f3f3f3"/>
        </linearGradient>
        <linearGradient id="purple-fade" x1="0" y1="0" x2="0" y2="1">
          <stop offset="0" stop-color="#9e4a7c"/><stop offset="1" stop-color="#c88aaa"/>
        </linearGradient>
      </defs>
      <rect width="300" height="162" fill="url(#grey-fade)"/>
      <polygon points="0,0 300,0 300,34 150,100 0,34" fill="url(#purple-fade)"/>
    </svg>
    <p class="model-text top-down"><strong>Top-down<br>‘Relationship’ NAS</strong><br>to display and enforce<br>top-management commitment</p>
    <p class="model-text bottom-up"><strong>Bottom-up<br>‘Touchpoint’ NAS</strong><br>focus frontline staff<br>on customer needs</p>
  </section>

  <section class="model-box model-right">
    <svg width="339" height="162" aria-hidden="true">
      <defs>
        <linearGradient id="purple-band" x1="0" y1="0" x2="0" y2="1">
          <stop offset="0" stop-color="#9e4a7c"/><stop offset="1" stop-color="#c48ba8"/>
        </linearGradient>
      </defs>
      <rect width="339" height="162" fill="url(#grey-fade)"/>
      <rect width="339" height="82" fill="url(#purple-band)"/>
    </svg>
    <ul class="bullet-list bullets-top">
      <li>Periodic <strong>Benchmarking</strong> of customers with key competitors and development over time</li>
      <li><strong>Mandatory Group KPI</strong> to measure customer loyalty with a common single measure</li>
      <li>Used for <strong>management incentives</strong>/ customer target setting</li>
    </ul>
    <ul class="bullet-list bullets-bottom">
      <li><strong>Change management tool</strong> to focus staff on customer needs at critical touchpoints</li>
      <li>Embeds <strong>performance measurement</strong> and <strong>customer feedback</strong> loops between front-line and customers</li>
    </ul>
  </section>

  <div class="segments" role="img" aria-label="Row of customer silhouettes grouped as detractors, passives and promoters"></div>
  <span class="segment-label label-detractors">Detractors</span>
  <span class="segment-label label-passives">Passives</span>
  <span class="segment-label label-promoters">Promoters</span>
  <div class="score-bar">
    <span class="score-name">Net Advocate Score</span>
    <span class="score-op">=</span>
    <span class="score-promoters">%Promoters</span>
    <span class="score-op">+</span>
    <span class="score-detractors">%Detractors</span>
  </div>

  <section class="system">
    <h1 class="system-title">The NET Advocate System</h1>

    <h2 class="step-title step-1"><b>Step 1:</b> Sort Customers</h2>
    <div class="sentiment s-promoters"><div class="sentiment-icon" role="img" aria-label="Happy customer icon"></div><span class="tag">Promoters</span></div>
    <div class="sentiment s-passives"><div class="sentiment-icon" role="img" aria-label="Neutral customer icon"></div><span class="tag">Passives</span></div>
    <div class="sentiment s-detractors"><div class="sentiment-icon" role="img" aria-label="Unhappy customer icon"></div><span class="tag">Detractors</span></div>

    <h2 class="step-title step-2"><b>Step 2:</b> Close the Loop</h2>
    <div class="customer-figure" role="img" aria-label="Customer silhouette"></div>
    <span class="customer-label">Customers</span>
    <span class="dialogue">Dialogue</span>
    <svg class="loop-lines" width="30" height="90" aria-hidden="true">
      <path d="M0 45 H12 M12 9 V75 M12 9 H30 M12 42 H30 M12 75 H30" stroke="#555" stroke-width="2" fill="none"/>
    </svg>
    <div class="role-box r1">Front Line</div>
    <div class="role-box r2">Manager</div>
    <div class="role-box r3">Execs</div>
    <span class="learn">Learn + Improve</span>

    <h2 class="step-title step-3"><b>Step 3:</b> Make Loyality a Top Priority</h2>
    <div class="priority p-sight">
      <div class="advocate-icon">
        <div class="advocate-head" role="img" aria-label="Employee icon"></div>
        <div class="advocate-bubble">NAS</div>
      </div>
      Line of Sights<br>for all Employers
    </div>
    <div class="priority p-champions">
      <svg width="136" height="60" viewBox="0 0 136 60" aria-hidden="true">
        <rect x="2" y="22" width="44" height="38" rx="3" fill="#555"/>
        <rect x="46" y="4" width="44" height="56" rx="3" fill="#666"/>
        <rect x="90" y="30" width="44" height="30" rx="3" fill="#555"/>
        <text x="24" y="48" fill="#fff" font-size="18" font-weight="700" text-anchor="middle">2</text>
        <text x="68" y="30" fill="#fff" font-size="18" font-weight="700" text-anchor="middle">1</text>
        <text x="112" y="52" fill="#fff" font-size="18" font-weight="700" text-anchor="middle">3</text>
      </svg>
      Celebrate Loyality<br>Champions
    </div>
    <div class="priority p-report">
      <svg width="70" height="70" viewBox="0 0 70 70" aria-hidden="true">
        <path d="M6 2 V66 H68" stroke="#555" stroke-width="2" fill="none"/>
        <path d="M8 40 L16 30 L22 36 L30 22 L38 30 L46 20 L54 28 L62 16 L66 22 V64 H8 Z" fill="#bbb"/>
        <path d="M8 40 L16 30 L22 36 L30 22 L38 30 L46 20 L54 28 L62 16 L66 22" stroke="#444" stroke-width="2" fill="none"/>
        <path d="M8 50 L18 44 L28 48 L38 40 L48 44 L58 36 L66 40" stroke="#444" stroke-width="2" fill="none"/>
      </svg>
      Report NAS Along<br>with Financial Metrics
    </div>
  </section>

</main>
</body>
</html>
```